Sports Betting

The principal project of the Company shall be a website for the conducting of “Calcutta-style” betting on a wide range of events

I'm looking for a design for my sports betting site.

here's what we have so far:

http://quilnaxo.com/

http://www.varmotide.com/Misc_optics/Best16_4/code-3/

Please use the logo for this site in your design:

Updates

Target Market(s)

OUR MISSION IS SIMPLE: MAKE SPORTS-RELATED LIVE DATA AND ODDS SOLUTIONS AN ASSET FOR YOUR BUSINESS NOT A PROBLEM.

We strive to make sports-related live data and odds solutions integrate seamlessly with your business so your business can grow. As your sports data partner, when your business grows ours will grow with you: therefore, we will work hand in hand with you to support your business success. Plovenwick’s core activities deal with facts from the world of sports; a world characterised by its high level of emotion. Plovenwick offers data for all types of popular sports, and provides a comprehensive, rapid and reliable service. We are pursuing the joint mission of Superior User Experience & Simplicity, based on broad knowledge of markets and customers in conjunction with innovation and technology expertise.

The operating activities include the collection, processing, monitoring and marketing of sports data. The result is a diverse portfolio of sports data products for you and your clients.

Industry/Entity Type

It Company

Requirements
Must have
• We're looking for an out of the box design to set us apart from our competition.

```html
<!DOCTYPE html>
<html lang="en">
<head>
<meta charset="utf-8">
<title>Varmotide Bet</title>
<link href="https://fonts.googleapis.com/css2?family=Roboto:ital,wght@0,400;0,500;0,700;1,400&display=swap" rel="stylesheet">
<style>
:root{
  --black:#000;
  --page:#efefef;
  --panel:#fff;
  --line:#cfcfcf;
  --text:#111;
  --muted:#555;
  --blue:#1aa3e0;
  --blue-dark:#0a7fb5;
  --red:#d40f0f;
  --red-dark:#a00000;
  --grey-bar:#d6d6d6;
  --ad:#e4e4e4;
}
*{box-sizing:border-box;margin:0;padding:0}
html,body{width:678px;height:1200px;overflow:hidden}
body{position:relative;background:var(--page);font-family:'Roboto',sans-serif;color:var(--text)}
a{color:inherit;text-decoration:none}
.site-header{position:absolute;left:0;top:0;width:678px;height:56px;background:var(--black)}
.brand{position:absolute;left:86px;top:10px;display:flex;align-items:center;gap:5px;color:#fff;font-weight:700;font-size:13px}
.brand-dot{width:12px;height:12px;border-radius:50%;background:var(--red)}
.login{position:absolute;top:8px;left:348px;display:flex;gap:3px}
.login .field{width:80px;height:14px;background:#fff;font-size:5.5px;color:#aaa;padding:4px 4px;font-style:italic}
.btn{display:inline-block;border-radius:7px;color:#fff;font-weight:700;font-size:5.5px;text-align:center;line-height:12px;height:12px;margin-top:1px}
.btn-blue{background:linear-gradient(var(--blue),var(--blue-dark))}
.btn-red{background:linear-gradient(#ee1c1c,var(--red-dark))}
.login .btn{width:34px}
.login .btn-red{width:43px}
.main-nav{position:absolute;top:38px;left:224px;width:370px;display:flex;justify-content:space-between;color:#fff;font-weight:700;font-size:7.5px}
.hero{position:absolute;left:85px;top:77px;width:508px;height:211px;background:linear-gradient(160deg,#3a4a2e,#161c12 60%,#2a2020)}
.hero-caption{position:absolute;left:0;bottom:0;width:100%;height:23px;background:rgba(30,30,30,.85);display:flex;align-items:center;justify-content:space-between;padding:0 6px}
.hero-caption span{color:var(--blue);font-size:10.5px;font-weight:500;flex:1;margin-left:10px}
.panel{position:absolute;background:var(--panel);border:1px solid var(--line)}
.panel-title{height:21px;background:var(--black);color:#fff;font-weight:700;font-size:7px;line-height:21px;padding-left:8px}
.betting{left:85px;top:302px;width:400px;height:344px}
.filters{height:21px;background:var(--grey-bar);display:flex;align-items:center;padding-left:8px;font-size:6px}
.filters label{display:flex;align-items:center;margin-right:8px}
.box{width:6px;height:6px;border:1px solid #888;background:#fff;margin-right:3px;position:relative}
.box.on::after{content:"";position:absolute;left:1px;top:0;width:2px;height:3px;border:solid #333;border-width:0 1px 1px 0;transform:rotate(45deg)}
.lines{width:384px;margin:12px 0 0 8px;border-collapse:collapse;font-size:5.8px}
.lines th{font-weight:400;font-style:italic;text-align:left;height:10px;border-bottom:1px solid #333}
.lines td{height:22.2px;border-bottom:1px solid #ddd;font-weight:700}
.lines td.act{text-align:right;white-space:nowrap}
.lines .btn{width:31px}
.lines .btn-red{width:41px;margin-left:2px}
.sidebar-list{list-style:none;padding:6px 8px;font-size:6px}
.sidebar-list li{line-height:12.7px}
.sidebar-list li::before{content:">";margin-right:4px;color:#555}
.categories{left:498px;top:302px;width:95px;height:222px}
.past{left:498px;top:537px;width:95px;height:215px}
.past li{line-height:8.6px;margin-bottom:5px;display:flex}
.past li::before{flex:none}
.past .date{display:block;text-align:right;font-style:italic;font-size:4.5px;color:#888}
.view-all{display:block;text-align:right;color:var(--blue);font-style:italic;font-size:5.5px;font-weight:500;text-decoration:underline;padding-right:8px}
.ad{position:absolute;left:498px;width:95px;height:80px;background:radial-gradient(#f4f4f4,var(--ad));color:#999;font-size:6px;letter-spacing:1px;display:flex;align-items:center;justify-content:center}
.news{left:85px;top:660px;width:400px;height:313px;overflow:hidden}
.news-item{display:flex;gap:8px;margin:10px 8px 0;height:78px;border-bottom:1px solid #ccc;overflow:hidden}
.news-item:first-of-type{margin-top:13px}
.news-photo{width:106px;height:66px;flex:none}
.news-item h3{font-size:8.3px;font-weight:500;margin-top:1px}
.news-item .date{font-size:4.5px;font-style:italic;color:#888;margin:2px 0 5px}
.news-item p{font-size:5.8px;line-height:10px;color:#333}
.news-item p a{color:var(--blue);font-style:italic;text-decoration:underline}
.news .view-all{margin-top:8px}
.site-footer{position:absolute;left:0;top:995px;width:678px;height:205px;background:var(--black);color:#bbb}
.footer-cols{position:absolute;left:85px;top:18px;width:508px;display:flex;justify-content:space-between}
.footer-col{width:117px}
.footer-col h4{font-size:6.5px;font-weight:700;color:#ccc;padding-bottom:4px;border-bottom:1px solid #555;margin-bottom:6px}
.footer-col li{list-style:none;font-size:6px;line-height:10px}
.footer-col li::before{content:"> "}
.social{display:flex;gap:3px}
.social span{width:13px;height:13px;border-radius:50%;background:#777}
.footer-rule{position:absolute;left:85px;top:95px;width:508px;border-top:1px solid #555}
.accept{position:absolute;top:115px;left:0;width:100%;display:flex;justify-content:center;align-items:center;gap:3px;font-size:6.5px;font-weight:700;color:#ccc}
.accept b{margin-right:4px}
.card{width:18px;height:10px;background:#ddd;border-radius:1px}
.terms{position:absolute;left:85px;top:137px;width:508px;text-align:center;font-size:5px;line-height:8.3px;color:#aaa}
.terms b{color:#ddd}
.copyright{position:absolute;top:181px;width:100%;text-align:center;font-size:5.2px;color:#aaa}
</style>
</head>
<body>
<header class="site-header">
  <a class="brand" href="#"><span class="brand-dot"></span>Varmotide Bet</a>
  <form class="login">
    <span class="field">Email</span><span class="field">Password</span>
    <span class="btn btn-blue">LOGIN</span><span class="btn btn-red">JOIN NOW</span>
  </form>
  <nav class="main-nav"><a href="#">SPORTS</a><a href="#">LIVE BETTING</a><a href="#">FEATURES</a><a href="#">NEWS</a><a href="#">PROMOTIONS</a><a href="#">CONTACT</a></nav>
</header>

<section class="hero" role="img" aria-label="Photo of two footballers contesting the ball on a pitch">
  <div class="hero-caption">
    <svg width="7" height="9" viewBox="0 0 7 9"><path d="M6 1L2 4.5L6 8" stroke="#ccc" stroke-width="1.6" fill="none"/></svg>
    <span>Ttile/Caption goes here</span>
    <svg width="7" height="9" viewBox="0 0 7 9"><path d="M1 1L5 4.5L1 8" stroke="#ccc" stroke-width="1.6" fill="none"/></svg>
  </div>
</section>

<section class="panel betting">
  <h2 class="panel-title">BETTING LINES</h2>
  <div class="filters">
    <label><i class="box on"></i>Golf</label><label><i class="box on"></i>Soccer</label><label><i class="box"></i>Tennis</label><label><i class="box"></i>Ice Hockey</label><label><i class="box on"></i>American Footbal</label><label><i class="box"></i>Specials</label><label><i class="box on"></i>Baseball</label><label><i class="box"></i>All</label>
  </div>
  <table class="lines">
    <thead><tr><th style="width:214px">Tournament</th><th style="width:40px">Limit</th><th style="width:58px">Total Bids</th><th></th></tr></thead>
    <tbody>
      <tr><td>Kelvar Open in Solmara</td><td>10K</td><td>$550,000.00</td><td class="act"><span class="btn btn-blue">SAVE</span><span class="btn btn-red">BET NOW</span></td></tr>
      <tr><td>Tessaro Golf Champions</td><td>25K</td><td>$5,550.00</td><td class="act"><span class="btn btn-blue">SAVE</span><span class="btn btn-red">BET NOW</span></td></tr>
      <tr><td>Brindle Challenge in partnership with the Ashcombe Foundation</td><td>10K</td><td>$5,234.00</td><td class="act"><span class="btn btn-blue">SAVE</span><span class="btn btn-red">BET NOW</span></td></tr>
      <tr><td>Orvanta Norvane Golf Championship</td><td>5K</td><td>$662.35</td><td class="act"><span class="btn btn-blue">SAVE</span><span class="btn btn-red">BET NOW</span></td></tr>
      <tr><td>Kovari Electric Championship at Varenhoe</td><td>10K</td><td>$20,000.00</td><td class="act"><span class="btn btn-blue">SAVE</span><span class="btn btn-red">BET NOW</span></td></tr>
      <tr><td>Meridbank Teloran Masters presented by Pelican Energy</td><td>50K</td><td>$5,000.00</td><td class="act"><span class="btn btn-blue">SAVE</span><span class="btn btn-red">BET NOW</span></td></tr>
      <tr><td>Harrowfield Insurance Open</td><td>25K</td><td>$250.00</td><td class="act"><span class="btn btn-blue">SAVE</span><span class="btn btn-red">BET NOW</span></td></tr>
      <tr><td>Cleanline Dunmark Open</td><td>100K</td><td>$195,000.00</td><td class="act"><span class="btn btn-blue">SAVE</span><span class="btn btn-red">BET NOW</span></td></tr>
      <tr><td>Kelvar Open in Solmara</td><td>10K</td><td>$550,000.00</td><td class="act"><span class="btn btn-blue">SAVE</span><span class="btn btn-red">BET NOW</span></td></tr>
      <tr><td>Tessaro Golf Champions</td><td>25K</td><td>$5,550.00</td><td class="act"><span class="btn btn-blue">SAVE</span><span class="btn btn-red">BET NOW</span></td></tr>
      <tr><td>Brindle Challenge in partnership with the Ashcombe Foundation</td><td>10K</td><td>$5,234.00</td><td class="act"><span class="btn btn-blue">SAVE</span><span class="btn btn-red">BET NOW</span></td></tr>
      <tr><td>Orvanta Norvane Golf Championship</td><td>5K</td><td>$662.35</td><td class="act"><span class="btn btn-blue">SAVE</span><span class="btn btn-red">BET NOW</span></td></tr>
    </tbody>
  </table>
</section>

<aside class="panel categories">
  <h2 class="panel-title">SPORTS CATEGORIES</h2>
  <ul class="sidebar-list">
    <li>Golf</li><li>Soccer - Matches</li><li>Soccer - Long Term</li><li>Asian Handicap</li><li>Tennis</li><li>Ice Hockey</li><li>American Footbal</li><li>Voleyball</li><li>Trotting</li><li>Specials</li><li>Baseball</li><li>Basketball</li><li>Boxing</li><li>Darts</li><li>Handball</li>
  </ul>
</aside>

<aside class="panel past">
  <h2 class="panel-title">PAST EVENTS</h2>
  <ul class="sidebar-list">
    <li><div>Kelvar Open in Solmara<span class="date">1/10/2013 - 1/13/2013</span></div></li>
    <li><div>Tessaro Golf Champions<span class="date">1/10/2013 - 1/13/2013</span></div></li>
    <li><div>Brindle Challenge in partnership with the Ashcombe Foundation<span class="date">1/17/2013 - 1/20/2013</span></div></li>
    <li><div>Orvanta Norvane Golf Championship<span class="date">1/17/2013 - 1/20/2013</span></div></li>
    <li><div>Kovari Electric Championship at Varenhoe<span class="date">1/18/2013 - 1/20/2013</span></div></li>
    <li><div>Cleanline Dunmark Open<span class="date">1/31/2013 - 2/3/2013</span></div></li>
  </ul>
  <a class="view-all" href="#">&gt; view all</a>
</aside>

<div class="ad" style="top:765px">180 x 150 Ad</div>
<div class="ad" style="top:857px">180 x 150 Ad</div>

<section class="panel news">
  <h2 class="panel-title">RECENT NEWS</h2>
  <article class="news-item">
    <div class="news-photo" role="img" aria-label="Photo of American football players on the field" style="background:linear-gradient(135deg,#3d6b4a,#1f3a2c 55%,#c9c9c9)"></div>
    <div><h3>Lorem Ipsum Dolor Sit Amet</h3><div class="date">8/06/2013</div>
    <p>Lorem ipsum dolor sit amet, consectetur adipiscing elit. Nunc volutpat mi nec lorem condimentum ultricies. Nam eu eros sit amet ante sollicitudin euismod lacinia ac lectus. Quisque at odio diam. Cras consequat pulvinar nisl sed ullamcorper. Nam ut condimentum magna, nec sodales nulla. Sed facilisis... <a href="#">&gt; read more</a></p></div>
  </article>
  <article class="news-item">
    <div class="news-photo" role="img" aria-label="Photo of basketball players celebrating on court" style="background:linear-gradient(135deg,#7a1418,#2a1a1a 60%,#9a5a3a)"></div>
    <div><h3>Pellentesque Lacerat Ectus Quis Est Venenatis</h3><div class="date">8/01/2013</div>
    <p>Pellentesque placerat lectus quis est venenatis, feugiat fermentum nibh venenatis. Cras scelerisque arcu lobortis lorem interdum, non feugiat felis hendrerit. Morbi id nisl at justo vestibulum suscipit. Pellentesque lobortis feugiat ultricies. Vivamus a risus eu ante aliquam... <a href="#">&gt; read more</a></p></div>
  </article>
  <article class="news-item">
    <div class="news-photo" role="img" aria-label="Photo of a golfer celebrating in front of a crowd" style="background:linear-gradient(135deg,#8a8a6a,#e6e6e0 50%,#4a6a3a)"></div>
    <div><h3>Vestibulum Sapien Justo, Rutrum Auctor Sed Frmentum</h3><div class="date">7/28/2013</div>
    <p>Vestibulum sapien justo, rutrum ut auctor sed, fermentum at nisi. Sed at vestibulum elit. Vestibulum quis mi eget metus varius tincidunt. Vestibulum nisl est, porttitor sed vestibulum nec, egestas at nulla. In tristique arcu nec sem convallis, vitae blandit... <a href="#">&gt; read more</a></p></div>
  </article>
  <a class="view-all" href="#">&gt; view all</a>
</section>

<footer class="site-footer">
  <div class="footer-cols">
    <div class="footer-col"><h4>VARMOTIDE BET</h4><ul><li>About Us</li><li>Responsible Gaming</li><li>Terms of Use</li><li>Partner with Us</li></ul></div>
    <div class="footer-col"><h4>CUSTOMER SERVICE</h4><ul><li>Help</li><li>Contact Us</li><li>FAQs</li></ul></div>
    <div class="footer-col"><h4>ACCOUNT</h4><ul><li>My Account</li><li>Register</li><li>Forgot Password?</li></ul></div>
    <div class="footer-col"><h4>CONNECT</h4><div class="social"><span></span><span></span><span></span><span></span><span></span></div></div>
  </div>
  <div class="footer-rule"></div>
  <div class="accept"><b>WE ACCEPT</b><span class="card"></span><span class="card"></span><span class="card"></span><span class="card"></span><span class="card"></span><span class="card"></span></div>
  <p class="terms"><b>TERMS AND CONDITIONS:</b> Lorem ipsum dolor sit amet, consectetur adipiscing elit. Aliquam sit amet massa eros. Etiam condimentum feugiat nibh, eu gravida dui dignissim et. Donec dignissim tellus odio, non eleifend nunc molestie eget. Donec vel eros massa. Morbi vel mauris luctus, sodales mi id, posuere mauris. Sed in orci consequat, lacinia magna at, consequat lorem. Pellentesque habitant morbi tristique senectus et netus et malesuada fames ac turpis egestas. Quisque ullamcorper imperdiet imperdiet. Duis elementum lacus purus, in sagittis mauris luctus at. Etiam in molestie odio, suscipit facilisis ipsum. Maecenas ut bibendum eros, auctor ornare tortor. Phasellus aliquet, ipsum quis ornare egestas, est purus ornare nulla, in scelerisque nunc massa vel orci.</p>
  <p class="copyright">© 2013 Varmotide Bet Limited.</p>
</footer>
</body>
</html>
```